Stationary design for a bidet toilet seat
Vellora Bidets
Stationary design for a bidet toilet seat  - Health
Creative Brief
Bright & Fun-filled
Tobias Merrick III
Marketing Agent
418 Westmere Ave. Suite 203 Houston, TX 77024
vellorabidets@quillpost-mail.com
My logo was done by Quorvan designs

```html
<!DOCTYPE html>
<html lang="en">
<head>
<meta charset="utf-8">
<title>Vellora Bidets – Business Card</title>
<link href="https://fonts.googleapis.com/css2?family=Cinzel:wght@400;600&family=Libre+Baskerville:wght@400&display=swap" rel="stylesheet">
<style>
  :root{
    --stage:#6e6e70;
    --blue:#2a82d3;
    --blue-deep:#1b64b3;
    --blue-light:#5aa8ea;
    --green:#4f9a2f;
    --paper:#ffffff;
    --paper-shade:#eef1f4;
    --ink:#3b3b3b;
  }
  *{margin:0;padding:0;box-sizing:border-box}
  html,body{width:1200px;height:908px;overflow:hidden}
  body{background:var(--stage);position:relative;font-family:"Libre Baskerville",Georgia,serif}
  .card{position:absolute;top:304px;width:510px;height:300px;border-radius:20px;overflow:hidden;
    box-shadow:0 10px 24px rgba(0,0,0,.35)}
  .card-front{left:70px;background:linear-gradient(135deg,var(--blue-light) 0%,var(--blue) 45%,var(--blue-deep) 100%)}
  .card-back{left:620px;background:linear-gradient(180deg,var(--paper) 0%,var(--paper) 70%,var(--paper-shade) 100%)}
  .front-wordmark{position:absolute;right:42px;top:118px;color:#fff;font-family:"Cinzel",Georgia,serif;
    font-weight:400;font-size:30px;letter-spacing:2px;white-space:nowrap}
  .swoosh{position:absolute;top:0;right:0;width:510px;height:300px}
  .person{position:absolute;left:250px;top:96px;text-align:left}
  .person-name{font-family:"Cinzel",Georgia,serif;font-weight:400;font-size:19px;color:var(--green);letter-spacing:1px;white-space:nowrap}
  .person-role{font-family:"Cinzel",Georgia,serif;font-size:10px;color:var(--blue);letter-spacing:1.5px;margin-top:4px}
  .brand{position:absolute;left:34px;top:140px;display:flex;align-items:center;gap:10px}
  .brand-dot{width:34px;height:34px;border-radius:50%;background:var(--blue)}
  .brand-name{font-family:"Cinzel",Georgia,serif;font-weight:400;font-size:20px;color:var(--green);letter-spacing:1px;white-space:nowrap}
  .contact{position:absolute;left:34px;top:188px;font-size:11px;line-height:14px;color:var(--ink)}
  .contact-line{display:flex;align-items:center;gap:6px;white-space:nowrap}
  .contact-icon{width:12px;height:12px;flex:none}
</style>
</head>
<body>
  <section class="card card-front">
    <div class="front-wordmark">Vellora Bidets</div>
  </section>

  <section class="card card-back">
    <svg class="swoosh" viewBox="0 0 510 300" aria-hidden="true">
      <path d="M250 0 C330 40 420 40 510 60 L510 0 Z" fill="#2a82d3"/>
      <path d="M200 0 C300 55 410 52 510 72" fill="none" stroke="#4f9a2f" stroke-width="4"/>
      <path d="M0 290 C150 282 340 286 510 270 L510 300 L0 300 Z" fill="#2a82d3" opacity=".9"/>
    </svg>

    <div class="person">
      <div class="person-name">Tobias Merrick III</div>
      <div class="person-role">Marketing Agent</div>
    </div>

    <div class="brand">
      <span class="brand-dot"></span>
      <span class="brand-name">Vellora Bidets</span>
    </div>

    <div class="contact">
      <div>418 Westmere Ave.</div>
      <div>Suite 203</div>
      <div>Houston, TX 77024</div>
      <div class="contact-line">
        <svg class="contact-icon" viewBox="0 0 12 12"><circle cx="6" cy="6" r="6" fill="#4f9a2f"/><path d="M4 3.2l1 1.6-.6.7a4 4 0 0 0 2.1 2.1l.7-.6 1.6 1-.6 1C6 9 3 6 3 3.8z" fill="#fff"/></svg>
        832.555.0142
      </div>
      <div class="contact-line">
        <svg class="contact-icon" viewBox="0 0 12 12"><circle cx="6" cy="6" r="6" fill="#4f9a2f"/><path d="M4 3.2l1 1.6-.6.7a4 4 0 0 0 2.1 2.1l.7-.6 1.6 1-.6 1C6 9 3 6 3 3.8z" fill="#fff"/></svg>
        832.555.0187
      </div>
      <div class="contact-line">
        <svg class="contact-icon" viewBox="0 0 12 12"><circle cx="6" cy="6" r="6" fill="#4f9a2f"/><rect x="3" y="4" width="6" height="4.2" fill="none" stroke="#fff" stroke-width=".9"/><path d="M3 4l3 2.4L9 4" fill="none" stroke="#fff" stroke-width=".9"/></svg>
        vellorabidets@quillpost-mail.com
      </div>
    </div>
  </section>
</body>
</html>
```